Varnek Group Business Card

Varnek Group — Business Card Design Brief
Overview
Design a double-sided business card for Varnek Group that highlights our two service arms: Varnek Communications (telecommunications) and Varnek Energy (business energy solutions). The card should feel smart and stand out when handed to clients.

Objectives
Showcase our areas of specialty clearly.
Reflect the overall Varnek / Varnek Group brand while acknowledging both arms.
Explore using both logos (Communications + Energy) or one unified logo, depending on the design.

Deliverables
One double-sided business card design (front + back).

Content & Copy
Front (preferred): Logo: Varnek / Varnek Group
Descriptor: Business Communications | Business Energy
Back:My contact details and company details
Core products: Business Mobile • Telephony • Internet • Business Energy Solutions

Brand & Visual Direction
We have a group logo currently tailored more toward telecoms, plus a separate Varnek Energy logo.
Please explore layouts that use both logos or just one, whichever works best.
Color: I wouldn't mind seeing an option using our the Blue/Purple gradient from our website (varnek-example.co.uk), but also open to non-gradient approaches and other colours..

Overall look: Smart, modern, and distinctive.
Format & Print Specs
Double-sided business card format. (Use a standard size

Must-Haves
Front: Varnek wording or Varnek Group wording with atleast 1 logo also on front “Business Communications | Business Energy.”

Back: Contact + company details and core products.
A design that stands out while remaining professional.

Nice-to-Have Options
A gradient version using our site’s Blue/Purple gradient.
A non-gradient version.
A dual-logo treatment versus a single-logo treatment.

Thanks
Dominic

```html
<!DOCTYPE html>
<html lang="en">
<head>
<meta charset="utf-8">
<title>Varnek Group Business Card</title>
<link href="https://fonts.googleapis.com/css2?family=Arimo:wght@400;700&display=swap" rel="stylesheet">
<style>
  :root {
    --backdrop: #ececec;
    --card-white: #ffffff;
    --navy: #1b1a6b;
    --green: #3aaa35;
    --text-grey: #4d4d4d;
    --tagline: #222222;
    --gradient-top: #d8d600;
    --gradient-bottom: #1ea30b;
    --white: #ffffff;
  }
  * { margin: 0; padding: 0; box-sizing: border-box; }
  html, body {
    width: 1200px; height: 1200px; overflow: hidden;
    background: var(--backdrop);
    font-family: "Arimo", Arial, sans-serif;
  }
  .canvas { position: relative; width: 1200px; height: 1200px; }

  .card {
    position: absolute;
    width: 689px; height: 394px;
    box-shadow: 0 10px 22px rgba(0,0,0,0.18);
  }
  .card-front { left: 256px; top: 158px; background: var(--card-white); }
  .card-back {
    left: 256px; top: 653px;
    background: linear-gradient(to bottom, var(--gradient-top), var(--gradient-bottom));
  }

  /* Front */
  .brand-mark { position: absolute; left: 96px; top: 106px; width: 92px; height: 92px; border-radius: 50%; background: var(--green); }
  .brand-name {
    position: absolute; left: 96px; top: 222px;
    font-size: 54px; font-weight: 700; color: var(--navy); letter-spacing: 1px; line-height: 1;
  }
  .front-divider { position: absolute; left: 370px; top: 74px; width: 1px; height: 235px; background: #cfcfcf; }
  .person { position: absolute; left: 395px; top: 88px; }
  .person-name { font-size: 26px; font-weight: 700; color: var(--navy); letter-spacing: 0.5px; line-height: 1.1; }
  .person-role { font-size: 15px; color: var(--green); margin-top: 1px; }
  .address { position: absolute; left: 395px; top: 157px; font-size: 16px; line-height: 21px; color: var(--text-grey); }
  .contact-list { position: absolute; left: 395px; top: 210px; list-style: none; }
  .contact-list li { display: flex; align-items: center; height: 20.5px; font-size: 16px; color: var(--text-grey); }
  .contact-list svg { width: 14px; height: 14px; margin-right: 12px; fill: var(--navy); flex: none; }
  .core-products {
    position: absolute; left: 0; right: 0; top: 340px;
    text-align: center; font-size: 17px; color: var(--tagline);
  }

  /* Back */
  .back-divider { position: absolute; left: 344px; top: 114px; width: 1px; height: 165px; background: rgba(255,255,255,0.85); }
  .arm { position: absolute; top: 140px; width: 344px; text-align: center; color: var(--white); }
  .arm-left { left: 0; }
  .arm-right { left: 345px; }
  .arm-brand { display: flex; align-items: center; justify-content: center; height: 90px; }
  .arm-circle { width: 56px; height: 56px; border-radius: 50%; border: 6px solid var(--white); margin-right: 14px; }
  .arm-name { font-size: 38px; font-weight: 700; color: var(--white); letter-spacing: 1px; }
  .arm-label { margin-top: 34px; font-size: 16px; letter-spacing: 0.2px; }
</style>
</head>
<body>
<div class="canvas">

  <section class="card card-front">
    <div class="brand-mark"></div>
    <div class="brand-name">VARNEK</div>
    <div class="front-divider"></div>

    <div class="person">
      <div class="person-name">MARTIN HALE</div>
      <div class="person-role">President</div>
    </div>
    <div class="address">412 Larchwood Road<br>Kelburn, Canada 20418</div>

    <ul class="contact-list">
      <li><svg viewBox="0 0 24 24"><path d="M6.6 10.8a15.1 15.1 0 0 0 6.6 6.6l2.2-2.2c.3-.3.7-.4 1-.2 1.1.4 2.3.6 3.6.6.6 0 1 .4 1 1V20c0 .6-.4 1-1 1A17 17 0 0 1 3 4c0-.6.4-1 1-1h3.5c.6 0 1 .4 1 1 0 1.3.2 2.5.6 3.6.1.3 0 .7-.2 1z"/></svg>555-014-2871</li>
      <li><svg viewBox="0 0 24 24"><path d="M7 1h10a2 2 0 0 1 2 2v18a2 2 0 0 1-2 2H7a2 2 0 0 1-2-2V3a2 2 0 0 1 2-2zm0 3v14h10V4zm5 15.5a1 1 0 1 0 0 2 1 1 0 0 0 0-2z"/></svg>555-019-6403</li>
      <li><svg viewBox="0 0 24 24"><path d="M2 5h20v14H2zm2 2v.5l8 5.5 8-5.5V7zm0 3v7h16v-7l-8 5.5z"/></svg>info@varnek-example.com</li>
      <li><svg viewBox="0 0 24 24"><path d="M12 2a10 10 0 1 0 0 20 10 10 0 0 0 0-20zm-1 17.9A8 8 0 0 1 4.2 10L9 15v1a2 2 0 0 0 2 2zm6.9-2.5A2 2 0 0 0 16 16h-1v-3a1 1 0 0 0-1-1H8v-2h2a1 1 0 0 0 1-1V7h2a2 2 0 0 0 2-2v-.4a8 8 0 0 1 2.9 12.8z"/></svg>www.varnek-example.com</li>
    </ul>

    <div class="core-products">Business Mobile &nbsp;•&nbsp; Telephony &nbsp;•&nbsp; Internet &nbsp;•&nbsp; Business Energy Solutions</div>
  </section>

  <section class="card card-back">
    <div class="arm arm-left">
      <div class="arm-brand"><span class="arm-circle"></span><span class="arm-name">VARNEK</span></div>
      <div class="arm-label">BUSINESS COMMUNICATIONS</div>
    </div>
    <div class="back-divider"></div>
    <div class="arm arm-right">
      <div class="arm-brand"><span class="arm-circle"></span><span class="arm-name">VARNEK</span></div>
      <div class="arm-label">BUSINESS ENERGY</div>
    </div>
  </section>

</div>
</body>
</html>
```